Cat-products company needs smart, yet endearing, business card

We need a business card design for a new, but up-and-running, business based in Honolulu, Hawaii. The business is Purrlane Nest Co. Our first product is the most environmentally-friendly cat grass kit ever seen on the planet. Future products, currently in the R&D phase, will include a variety of exciting cat scratchers. We also do consulting work to help apartment-dwellers make their home more cat-friendly and, in the future, plan on doing full, custom installs of structure to create high walkways for cats.

Target Market(s)

Middle-aged, apartment-dwelling, middle-class workers who own 1 or more cats and who dote on them.

Industry/Entity Type

Pet Care

Contact Information for Business Card

A striking, professional, yet warm and friendly design is what we're after.

Font styles to use
Serif
Sans Serif
Other font styles liked:
• Comfortaa

Colors

Designer to choose colors to be used in the design.

Requirements
Must have
• The company logo: (see attachment)
• The company name: Purrlane Nest Co
• The web address: www.purrlanenestco.example
• Email: support@purrlanenestco.example
• Phone: +1 (808) 555 0172
• Update (Fri Jun 30 3017 7:45pm Hawaii Time) I would like, is possible, uploaded picture of the cat grass kit on the back of the card with some text along the lines of: Purrlane Nest Co - Where The Freshest Kitty Sprouts Begin
Nice to have
• A cat picture, cartoon, real or silhouette that illustrates cats in action and/or relaxing; ie using the apartment space to live, play and relax in and being well-contented.
• Most of the website is done in the font: Comfortaa. It might be nice to continue using this for brand consistency.
Should not have
• Hard-to-read fonts.

```html
<!DOCTYPE html>
<html lang="en">
<head>
<meta charset="utf-8">
<title>Purrlane Nest Co — Business Card</title>
<link rel="stylesheet" href="https://fonts.googleapis.com/css2?family=Quicksand:wght@500;700&display=swap">
<style>
  :root {
    --backdrop: #ececea;
    --card-light: #ffffff;
    --card-mid: #d8f3f6;
    --card-tint: #84dbe5;
    --teal: #1fb5bf;
    --brown: #5a2b25;
    --ink: #4a2420;
  }
  * { margin: 0; padding: 0; box-sizing: border-box; }
  html, body {
    width: 1200px;
    height: 961px;
    overflow: hidden;
    background: var(--backdrop);
    font-family: "Quicksand", sans-serif;
  }
  .sheet {
    position: relative;
    width: 1200px;
    height: 961px;
  }
  .card {
    position: absolute;
    left: 240px;
    width: 720px;
    height: 411px;
    border-radius: 4px;
    background: linear-gradient(155deg, var(--card-light) 18%, var(--card-mid) 52%, var(--card-tint) 100%);
    box-shadow: 0 10px 28px rgba(0, 0, 0, 0.16);
    overflow: hidden;
  }
  .card--front { top: 50px; }
  .card--back { top: 500px; }

  .brand-lockup {
    position: absolute;
    left: 0;
    right: 0;
    display: flex;
    align-items: center;
    justify-content: center;
    gap: 18px;
  }
  .brand-mark {
    flex: none;
    background: var(--brown);
    border-radius: 3px;
  }
  .brand-name {
    color: var(--teal);
    font-weight: 700;
    letter-spacing: 0.5px;
    line-height: 1;
    white-space: nowrap;
  }

  .card--front .brand-lockup {
    top: 50%;
    transform: translateY(-50%);
  }
  .card--front .brand-mark { width: 62px; height: 62px; }
  .card--front .brand-name { font-size: 54px; }

  .card--back .brand-lockup { top: 58px; }
  .card--back .brand-mark { width: 44px; height: 44px; }
  .card--back .brand-name { font-size: 38px; }

  .divider-dot {
    position: absolute;
    left: 50%;
    top: 150px;
    width: 22px;
    height: 22px;
    margin-left: -11px;
    border-radius: 50%;
    background: var(--brown);
  }
  .contact-list {
    position: absolute;
    left: 0;
    right: 0;
    top: 206px;
    list-style: none;
    text-align: center;
    color: var(--ink);
    font-weight: 500;
    font-size: 22px;
    line-height: 1.8;
  }
</style>
</head>
<body>
  <main class="sheet">
    <section class="card card--front" aria-label="Card front">
      <div class="brand-lockup">
        <span class="brand-mark" aria-hidden="true"></span>
        <p class="brand-name">Purrlane Nest Co</p>
      </div>
    </section>

    <section class="card card--back" aria-label="Card back">
      <div class="brand-lockup">
        <span class="brand-mark" aria-hidden="true"></span>
        <p class="brand-name">Purrlane Nest Co</p>
      </div>
      <span class="divider-dot" aria-hidden="true"></span>
      <ul class="contact-list">
        <li class="contact-web">www.purrlanenestco.example</li>
        <li class="contact-email">support@purrlanenestco.example</li>
        <li class="contact-phone">+1 (808) 555 0172</li>
      </ul>
    </section>
  </main>
</body>
</html>
```